Film Festival Poster Design Project

The 5th Annual Harrowgate Open Screen Festival will be taking place on November 12th in Wales at the Millbrook Picturehouse, Newport.

It is an all day event and there will be an eclectic mix of films on show.

Target Market(s)

Students 18-25

Industry/Entity Type

Festival

Requirements
Must have
• Title: 5th Harrowgate Open Screen Festival

Date: Saturday 12th November 2011

Place: Millbrook Playhouse & Picturehouse, Newport, Wales

Must include the text: BUY TICKETS ONLINE AT WWW.REELGATHERINGHUB.EXAMPLE

Sponsors & Festival Logo's must be included.
Nice to have
• As the festival is based in Wales, it would be nice to have a slightly Welsh tone to the poster, or a British feel.

```html
<!DOCTYPE html>
<html lang="en">
<head>
<meta charset="utf-8">
<title>5th Harrowgate Open Screen Festival 2011</title>
<link rel="stylesheet" href="https://fonts.googleapis.com/css2?family=Chewy&family=Archivo+Black&display=swap">
<style>
  :root {
    --festival-green: #1d5a17;
    --bright-green: #22d32c;
    --poster-red: #c3141b;
    --deep-red: #e0191d;
    --ink: #111111;
    --paper: #ffffff;
    --strip-red: #e5191c;
  }
  * { margin: 0; padding: 0; box-sizing: border-box; }
  html, body { width: 900px; height: 1200px; overflow: hidden; background: var(--paper); }
  .poster {
    position: relative; width: 900px; height: 1200px; overflow: hidden;
    background: linear-gradient(150deg, var(--bright-green) 0%, #8fe88a 22%, #ffffff 42%, #f7b9b6 60%, var(--deep-red) 92%);
    font-family: "Chewy", "Comic Sans MS", cursive;
  }
  .backdrop { position: absolute; inset: 0; }
  .dragon-motif {
    position: absolute; left: 90px; top: 300px; width: 720px; height: 400px;
    border-radius: 50%;
    background: radial-gradient(ellipse at center, rgba(230,40,40,0.28), rgba(230,40,40,0) 70%);
  }
  .text { position: absolute; text-align: center; line-height: 1; }
  .all-day { left: 0; top: 30px; width: 310px; color: var(--poster-red); font-size: 70px; line-height: 1.0; }
  .eclectic { left: 610px; top: 35px; width: 270px; color: var(--poster-red); font-size: 50px; line-height: 1.6; }
  .guild-badge {
    position: absolute; left: 356px; top: 5px; width: 190px; height: 278px;
    background: var(--paper); display: flex; flex-direction: column;
    align-items: center; justify-content: center; gap: 18px;
  }
  .guild-badge .mark { width: 90px; height: 90px; border-radius: 50%; background: var(--ink); }
  .guild-badge .name { font-size: 30px; color: var(--ink); text-align: center; line-height: 1.05; }
  .title { left: 0; top: 290px; width: 900px; color: var(--festival-green); font-size: 84px; line-height: 1.08; }
  .date-day { left: 60px; top: 725px; width: 320px; color: var(--ink); font-size: 66px; }
  .date-full { left: 0; top: 840px; width: 490px; color: var(--ink); font-size: 66px; }
  .venue { left: 545px; top: 720px; width: 350px; color: var(--ink); font-size: 36px; line-height: 1.35; }
  .tickets { left: 0; top: 942px; width: 900px; color: var(--festival-green); font-size: 54px; text-decoration: underline; text-decoration-thickness: 3px; text-underline-offset: 6px; }
  .web {
    left: 0; top: 1016px; width: 900px; color: var(--ink);
    font-family: "Archivo Black", "Arial Black", sans-serif; font-size: 37px;
    text-decoration: underline; text-decoration-thickness: 3px; text-underline-offset: 5px;
  }
  .film-strip { position: absolute; left: 0; top: 1072px; width: 900px; height: 100px; }
  .sponsor { position: absolute; display: flex; flex-direction: column; align-items: center; justify-content: center; text-align: center; font-size: 18px; }
  .sponsor-lantern { left: 0; top: 1102px; width: 128px; height: 66px; background: var(--ink); color: var(--paper); gap: 4px; }
  .sponsor-lantern .url { font-size: 9px; }
  .sponsor-westgate { left: 355px; top: 1112px; width: 170px; height: 56px; color: var(--ink); background: rgba(255,255,255,0.25); }
  .sponsor-bright { left: 760px; top: 1104px; width: 120px; height: 62px; background: var(--paper); color: var(--ink); font-size: 20px; }
  .camera-icon { position: absolute; top: 1086px; width: 70px; height: 62px; background: var(--ink); border-radius: 6px; opacity: 0.85; }
</style>
</head>
<body>
<main class="poster">
  <svg class="backdrop" width="900" height="1200" viewBox="0 0 900 1200" aria-hidden="true">
    <circle cx="470" cy="440" r="400" fill="#ffffff" fill-opacity="0.35"/>
    <circle cx="230" cy="780" r="320" fill="#ffffff" fill-opacity="0.3"/>
    <circle cx="690" cy="770" r="330" fill="#ffffff" fill-opacity="0.3"/>
  </svg>
  <div class="dragon-motif" role="img" aria-label="Faint red Welsh dragon motif behind the title"></div>

  <p class="text all-day">ALL DAY<br>EVENT!</p>

  <div class="guild-badge">
    <span class="mark"></span>
    <span class="name">Reel Gathering Hub</span>
  </div>

  <p class="text eclectic">Eclectic Mix<br>Of Films<br>On Show.</p>

  <h1 class="text title">5th Harrowgate<br>Open Screen<br>Festival<br>2011</h1>

  <p class="text date-day">Saturday</p>
  <p class="text date-full">12th November</p>
  <p class="text venue">Millbrook Playhouse<br>&amp; Picturehouse,<br>Newport, Wales</p>

  <p class="text tickets">Buy Your Tickets Online At</p>
  <p class="text web">WWW.REELGATHERINGHUB.EXAMPLE</p>

  <svg class="film-strip" width="900" height="100" viewBox="0 0 900 100" aria-hidden="true">
    <rect x="0" y="0" width="900" height="100" rx="12" fill="#111"/>
    <rect x="130" y="28" width="620" height="44" fill="var(--strip-red)"/>
    <g fill="#fff">
      <rect x="20" y="6" width="22" height="14"/><rect x="70" y="6" width="22" height="14"/>
      <rect x="120" y="6" width="22" height="14"/><rect x="170" y="6" width="22" height="14"/>
      <rect x="220" y="6" width="22" height="14"/><rect x="270" y="6" width="22" height="14"/>
      <rect x="320" y="6" width="22" height="14"/><rect x="370" y="6" width="22" height="14"/>
      <rect x="420" y="6" width="22" height="14"/><rect x="470" y="6" width="22" height="14"/>
      <rect x="520" y="6" width="22" height="14"/><rect x="570" y="6" width="22" height="14"/>
      <rect x="620" y="6" width="22" height="14"/><rect x="670" y="6" width="22" height="14"/>
      <rect x="720" y="6" width="22" height="14"/><rect x="770" y="6" width="22" height="14"/>
      <rect x="820" y="6" width="22" height="14"/>
      <rect x="20" y="80" width="22" height="14"/><rect x="70" y="80" width="22" height="14"/>
      <rect x="120" y="80" width="22" height="14"/><rect x="170" y="80" width="22" height="14"/>
      <rect x="220" y="80" width="22" height="14"/><rect x="270" y="80" width="22" height="14"/>
      <rect x="320" y="80" width="22" height="14"/><rect x="370" y="80" width="22" height="14"/>
      <rect x="420" y="80" width="22" height="14"/><rect x="470" y="80" width="22" height="14"/>
      <rect x="520" y="80" width="22" height="14"/><rect x="570" y="80" width="22" height="14"/>
      <rect x="620" y="80" width="22" height="14"/><rect x="670" y="80" width="22" height="14"/>
      <rect x="720" y="80" width="22" height="14"/><rect x="770" y="80" width="22" height="14"/>
      <rect x="820" y="80" width="22" height="14"/>
    </g>
    <rect x="340" y="28" width="8" height="44" fill="#111"/>
    <rect x="540" y="28" width="8" height="44" fill="#111"/>
  </svg>

  <div class="camera-icon" style="left:185px" role="img" aria-label="Film camera illustration"></div>
  <div class="camera-icon" style="left:635px" role="img" aria-label="Film camera illustration"></div>

  <div class="sponsor sponsor-lantern">
    <span>Lanternhill Films</span>
    <span class="url">www.lanternhillfilms.example</span>
  </div>
  <div class="sponsor sponsor-westgate"><span>Westgate Digital Works</span></div>
  <div class="sponsor sponsor-bright"><span>Brightfold</span></div>
</main>
</body>
</html>
```